依頼詳細
最低限の要件としては、下記のみとなりますが、
少しでも大学生・大学院生の応募が増えるようにセンスのあるチラシを作成したいと考えております。

■要件内容
①赤を基調とすること(赤色は昨年のチラシ、パンフ等で用いたテーマカラーです)
②昨年のイベントと同じことを示すため、KSTFおよびCampus Startup Flagship Cup という名称の使用
記載項目
・昨年のイベントと同じことを示すため、KSTFおよびCampus Startup Flagship Cup 2013という名称の使用

・記載する文字量は昨年のチラシとほぼ同様です。
現在調整中の内容が多く、情報が分かり次第、本募集へ追記、または当選となるデザインのご作成者様とのやりとりで、具体的文言を入れて頂くかたちをとらせて頂ければと思います。
サイズ
A4
ページ数
両面
希望イメージ
シンプル 複雑
単色 カラフル
暗い 明るい
日常 高級
遊び心 厳粛
未来的 伝統的
女性的 男性的
希望する色
赤を基調にして作成を御願い致します。
納品ファイル
• イラストレーター形式 (.ai)
補足説明
※去年のチラシを添付しておりますので、ご確認の上、作成をお願いいたします。
昨年チラシが添付漏れておりましたので、添付致します。
ご確認の上、作成をお願い致します。

壁をも壊しながら突き進む学生らしい躍動感が感じられ、大変気に入りました。よろしくお願いいたします。

皆様、多くのご応募大変ありがとうございました。よい提案がたくさんありまして、非常に迷いました。
今後ともどうぞよろしくお願いいたします。

```html
<!DOCTYPE html>
<html lang="ja">
<head>
<meta charset="utf-8">
<title>KSTF 2013 — Campus Startup Flagship Cup</title>
<link rel="stylesheet" href="https://fonts.googleapis.com/css2?family=Roboto:wght@700;900&family=Noto+Sans+JP:wght@400;500;700&display=swap">
<style>
  :root {
    --red: #e3101a;
    --black: #0c0c0c;
    --white: #ffffff;
    --ink: #1a1a1a;
  }
  * { margin: 0; padding: 0; box-sizing: border-box; }
  html, body { width: 851px; height: 1200px; overflow: hidden; background: var(--white); }
  .poster {
    position: relative; width: 851px; height: 1200px; overflow: hidden;
    background: var(--white); font-family: "Noto Sans JP", sans-serif;
  }
  .panel-red { position: absolute; left: 0; top: 0; width: 497px; height: 950px; background: var(--red); }
  .panel-black { position: absolute; left: 497px; top: 0; width: 354px; height: 950px; background: var(--black); }

  .mega-mark {
    position: absolute; left: 330px; top: 24px;
    transform: rotate(90deg); transform-origin: top left;
    font-family: "Roboto", sans-serif; font-weight: 900;
    font-size: 400px; line-height: 1; letter-spacing: -6px;
    color: var(--white); white-space: nowrap;
  }
  .vertical-name {
    position: absolute; left: 400px; top: 28px;
    transform: rotate(90deg); transform-origin: top left;
    font-family: "Roboto", sans-serif; font-weight: 700; white-space: nowrap; line-height: 1;
    font-size: 44px; color: var(--white);
  }

  .headline { position: absolute; left: 497px; top: 22px; width: 354px; text-align: center; color: var(--red); font-family: "Roboto", sans-serif; font-weight: 700; }
  .headline__name { font-size: 22px; line-height: 1.1; }
  .headline__mark { display: flex; justify-content: center; align-items: flex-start; gap: 8px; margin-top: 4px; }
  .headline__abbr { font-size: 82px; line-height: 0.95; font-weight: 900; letter-spacing: -1px; }
  .headline__year { writing-mode: vertical-rl; font-size: 26px; line-height: 1; margin-top: 6px; }
  .headline__date { margin-top: 10px; color: var(--white); font-size: 16px; font-weight: 700; }

  .idea-icon { position: absolute; left: 600px; top: 240px; width: 130px; height: 150px; }

  .figure-art {
    position: absolute; left: 480px; top: 430px; width: 260px; height: 510px;
    background: var(--white); border-radius: 46% 54% 30% 40% / 28% 30% 40% 36%;
  }

  .details { position: absolute; left: 48px; top: 962px; width: 760px; color: var(--ink); }
  .details__title { font-size: 17px; font-weight: 500; letter-spacing: 1px; }
  .details__row { font-size: 16px; font-weight: 500; line-height: 1.55; }
  .details__row:first-of-type { margin-top: 4px; }
  .details__small { margin-top: 8px; font-size: 9.5px; line-height: 1.6; color: var(--ink); }
</style>
</head>
<body>
<main class="poster">
  <div class="panel-red"></div>
  <div class="panel-black"></div>

  <div class="mega-mark">KSTF</div>
  <div class="vertical-name">Campus Startup Flagship Cup</div>

  <header class="headline">
    <p class="headline__name">Campus Startup Flagship Cup</p>
    <div class="headline__mark">
      <span class="headline__abbr">KSTF</span>
      <span class="headline__year">2013</span>
    </div>
    <p class="headline__date">22th December 2013 in RYOKUFU HALL</p>
  </header>

  <svg class="idea-icon" viewBox="0 0 130 150" fill="none" stroke="#ffffff" stroke-width="4" stroke-linecap="round">
    <line x1="65" y1="8" x2="65" y2="26"/>
    <line x1="22" y1="26" x2="34" y2="38"/>
    <line x1="108" y1="26" x2="96" y2="38"/>
    <line x1="6" y1="68" x2="22" y2="68"/>
    <line x1="108" y1="68" x2="124" y2="68"/>
    <path d="M65 40 C44 40 32 56 32 72 C32 88 46 96 50 110 L80 110 C84 96 98 88 98 72 C98 56 86 40 65 40 Z"/>
    <line x1="52" y1="120" x2="78" y2="120"/>
    <line x1="55" y1="130" x2="75" y2="130"/>
    <path d="M58 110 L62 86 L68 86 L72 110"/>
  </svg>

  <div class="figure-art" role="img" aria-label="白いシルエットの学生が壁を突き破るように腕を伸ばすイラスト"></div>

  <section class="details">
    <p class="details__title">ビジネスプランコンテスト全国大会２０１３</p>
    <p class="details__row">開 催 日 時 ： 平成25年12月22日（日）13：00〜（コンテスト等）18：10〜（懇親会）</p>
    <p class="details__row">開 催 場 所 ： 東都大学　緑風ホール（東京都中央区桜台）</p>
    <p class="details__row">プラン締切：11月15日（金）〜一般参加申込締切：11月30日（土）</p>
    <div class="details__small">
      <p>主　催：大学・大学院生起業支援ネットワーク　実行委員会</p>
      <p>共　催：東都大学産学連携本部　起業支援室</p>
      <p>後　援：一般社団法人ベンチャー育成協議会（予定）／公益財団法人未来創造基金（予定）／学生起業推進会議（予定）</p>
      <p>協　賛：地域産業振興センター／若手経営者フォーラム</p>
      <p>お問合せ：Campus Startup Flagship Cup 実行委員会　事務局　電話 03-0000-0000　https://kstf-cup.example.jp</p>
    </div>
  </section>
</main>
</body>
</html>
```